Golden Years Wellness Roadmap: This is my second book. The first was Eldercare Compass

I need a book cover design for: GOLDEN YEARS WELLNESS ROADMAP: A NO-EXPENSE METHOD FOR FINISHING YOUR LATER-LIFE MOSAIC WITH POOLED KVB CARE SCHEMES by Derek Holloway Neil Osgrove & Martin Quarles. This book is designed for business owners, CEO's, CFO's and Human Resources. The cover needs to be professional and focused on business. The purpose of this book is to educate business owners and their management about a zero cost retiree health plan. This is a first of it's kind solution that every business needs to learn about.

Target Market(s)

Business owners, CEO's, CFO's and Human Resources

Requirements
Nice to have
• I want the design to be clean and professional since it is focused on business executives

```html
<!DOCTYPE html>
<html lang="en">
<head>
<meta charset="utf-8">
<title>Golden Years Wellness Roadmap – Book Cover</title>
<link rel="stylesheet" href="https://fonts.googleapis.com/css2?family=Josefin+Sans:wght@300;400&family=Montserrat:wght@500;700&display=swap">
<style>
  :root {
    --page-bg: #eef0f3;
    --navy: #14276e;
    --royal: #1f3fa8;
    --electric: #2f6fd6;
    --glow: #f2c66d;
    --glow-soft: #f7e2a8;
    --paper: #f7f8fa;
    --ink: #1d2440;
    --teal: #1c7a8c;
    --white: #ffffff;
  }
  * { margin: 0; padding: 0; box-sizing: border-box; }
  html, body {
    width: 1200px;
    height: 1200px;
    overflow: hidden;
    background: var(--page-bg);
  }
  .stage {
    width: 1200px;
    height: 1200px;
    display: flex;
    align-items: center;
    justify-content: center;
  }
  .book-cover {
    width: 720px;
    height: 1080px;
    display: flex;
    flex-direction: column;
    box-shadow: 0 10px 30px rgba(20, 39, 110, 0.18);
    background: var(--paper);
  }
  .cover-art {
    height: 540px;
    background:
      radial-gradient(circle at 48% 52%, var(--glow-soft) 0%, var(--glow) 14%, rgba(47,111,214,0.9) 34%, var(--royal) 60%, var(--navy) 100%);
  }
  .title-band {
    height: 310px;
    background: var(--paper);
    display: flex;
    flex-direction: column;
    align-items: center;
    justify-content: center;
    text-align: center;
    padding: 0 40px;
    border-top: 6px solid var(--royal);
  }
  .title-main {
    font-family: "Josefin Sans", sans-serif;
    font-weight: 300;
    color: var(--ink);
    letter-spacing: 6px;
    line-height: 1.08;
  }
  .title-main .line-one { display: block; font-size: 40px; }
  .title-main .line-two { display: block; font-size: 46px; letter-spacing: 8px; }
  .subtitle {
    margin-top: 16px;
    font-family: "Josefin Sans", sans-serif;
    font-weight: 400;
    font-size: 18px;
    letter-spacing: 2px;
    color: var(--ink);
    line-height: 1.25;
  }
  .subtitle-accent {
    margin-top: 6px;
    font-family: "Montserrat", sans-serif;
    font-weight: 700;
    font-size: 22px;
    letter-spacing: 2px;
    color: var(--teal);
  }
  .author-band {
    flex: 1;
    background: linear-gradient(180deg, var(--navy) 0%, var(--royal) 55%, var(--electric) 100%);
    display: flex;
    flex-direction: column;
    align-items: center;
    padding-top: 34px;
  }
  .authors {
    font-family: "Montserrat", sans-serif;
    font-weight: 700;
    font-size: 25px;
    letter-spacing: 5px;
    color: var(--white);
    text-align: center;
    line-height: 1.4;
  }
</style>
</head>
<body>
<main class="stage">
  <article class="book-cover">
    <div class="cover-art" role="img" aria-label="Illustration of a person fitting together a glowing puzzle with a health emblem, beside palm trees on a blue digital backdrop"></div>
    <header class="title-band">
      <h1 class="title-main">
        <span class="line-one">GOLDEN YEARS WELLNESS</span>
        <span class="line-two">ROADMAP:</span>
      </h1>
      <p class="subtitle">A NO-EXPENSE METHOD<br>FOR FINISHING YOUR LATER-LIFE MOSAIC</p>
      <p class="subtitle-accent">WITH POOLED KVB CARE SCHEMES</p>
    </header>
    <footer class="author-band">
      <p class="authors">Derek Holloway, Neil Osgrove<br>&amp; Martin Quarles</p>
    </footer>
  </article>
</main>
</body>
</html>
```